This is a laser engraving business. I’m looking for a business card that includes a minimalist laser logo/design with the company name Brindle Crafts and telephone number 321-555-0148 and email brindlecrafts@mailbox.example

Industry/Entity Type

Laser engraving

Contact Information for Business Card

Laser logo/design that represents laser engraving

```html
<!DOCTYPE html>
<html lang="en">
<head>
<meta charset="utf-8">
<title>Brindle Crafts – Business Cards</title>
<link href="https://fonts.googleapis.com/css2?family=Michroma&family=Montserrat:wght@600&family=Arimo&display=swap" rel="stylesheet">
<style>
  :root {
    --page: #1c1c1c;
    --card: #111111;
    --ink-light: #ffffff;
    --ink-dark: #0d0d0d;
    --rule: #8a8a8a;
  }
  html, body {
    margin: 0;
    width: 1200px;
    height: 900px;
    overflow: hidden;
    background: var(--page);
  }
  .sheet {
    width: 1200px;
    height: 900px;
    display: flex;
    flex-direction: column;
    align-items: center;
    justify-content: center;
    gap: 40px;
  }
  .card {
    position: relative;
    width: 700px;
    height: 400px;
    background: var(--card);
    box-shadow: 0 10px 30px rgba(0,0,0,.5);
    overflow: hidden;
  }
  .brand {
    position: absolute;
    left: 0;
    right: 0;
    display: flex;
    flex-direction: column;
    align-items: center;
  }
  .card--front .brand { top: 70px; }
  .card--back .brand { top: 40px; }
  .brand__dot {
    width: 90px;
    height: 90px;
    border-radius: 50%;
    background: var(--ink-light);
  }
  .brand__name {
    margin-top: 26px;
    font-family: "Montserrat", sans-serif;
    font-weight: 600;
    font-size: 30px;
    letter-spacing: 0.5px;
    text-transform: uppercase;
    color: var(--ink-light);
  }
  .contact-email {
    margin-top: 14px;
    padding-top: 14px;
    border-top: 1px solid var(--rule);
    font-family: "Arimo", sans-serif;
    font-size: 26px;
    color: var(--ink-light);
  }
  .phone-band {
    position: absolute;
    left: 0;
    right: 0;
    bottom: 0;
    height: 96px;
    background: var(--ink-light);
    display: flex;
    align-items: center;
    justify-content: center;
  }
  .phone-band__number {
    font-family: "Michroma", sans-serif;
    font-size: 50px;
    font-weight: 700;
    letter-spacing: 2px;
    color: var(--ink-dark);
  }
</style>
</head>
<body>
  <main class="sheet">
    <section class="card card--front">
      <div class="brand">
        <div class="brand__dot"></div>
        <div class="brand__name">Brindle Crafts</div>
      </div>
      <div class="phone-band">
        <span class="phone-band__number">321-555-0148</span>
      </div>
    </section>

    <section class="card card--back">
      <div class="brand">
        <div class="brand__dot"></div>
        <div class="brand__name">Brindle Crafts</div>
        <div class="contact-email">brindlecrafts@mailbox.example</div>
      </div>
      <div class="phone-band">
        <span class="phone-band__number">321-555-0148</span>
      </div>
    </section>
  </main>
</body>
</html>
```